TORVEL Business Card Design

We need a business card design for a current Plastering company now moving to building and constructing new homes.
We have been in the Plastering(rendering) business for 15yrs and have made a good name with our customers for our Top Quality of work that we provide.
We would like TORVEL to be the main attraction with an image of architectural roof tops or house design within it. Blue Yellow and Black are colours we like but are willing to see other ideas.
We would like the design to be modern and communicate quality and experience.
Industry/Entity Type
Building
Contact Information for Business Card
TORVEL Building and Plastering
PO BOX 57390 Marlowe Darwin NT 0815
PH/Fax: 08 89317725 Email: torvel@quellnet.com
Dale: 0417396248 Rosa:0409273516
ABN:58 297 130 846

```html
<!DOCTYPE html>
<html lang="en">
<head>
<meta charset="utf-8">
<title>TORVEL Building and Plastering – Business Card</title>
<link rel="stylesheet" href="https://fonts.googleapis.com/css2?family=Open+Sans:wght@300;400;600;700&display=swap">
<style>
  :root {
    --backdrop: #ececec;
    --card-white: #ffffff;
    --brand-blue: #2e96d3;
    --ink-dark: #555555;
    --ink-mid: #606060;
    --shadow: rgba(0, 0, 0, 0.28);
  }
  * { margin: 0; padding: 0; box-sizing: border-box; }
  html, body {
    width: 1200px; height: 1200px; overflow: hidden;
    background: var(--backdrop);
    font-family: "Open Sans", Arial, sans-serif;
  }
  .card {
    position: absolute; left: 272px; width: 660px; height: 408px;
    box-shadow: 0 3px 8px var(--shadow);
  }
  .card--front { top: 123px; background: var(--card-white); }
  .card--back { top: 643px; background: var(--brand-blue); }

  .brand { position: absolute; display: flex; align-items: center; }
  .brand__mark { background: var(--brand-blue); }
  .brand__name { font-weight: 600; line-height: 1; letter-spacing: 1px; }

  .card--front .brand { left: 40px; top: 70px; gap: 18px; }
  .card--front .brand__mark { width: 58px; height: 58px; }
  .card--front .brand__name { font-size: 46px; color: var(--ink-dark); }

  .card--back .brand {
    left: 0; right: 0; top: 88px;
    flex-direction: column; gap: 26px;
  }
  .card--back .brand__mark { width: 110px; height: 110px; background: var(--card-white); }
  .card--back .brand__name { font-size: 78px; color: var(--card-white); }

  .company {
    position: absolute; right: 38px; top: 157px; text-align: right;
    color: var(--ink-dark);
  }
  .company__name { font-size: 19.5px; font-weight: 700; line-height: 28px; }
  .company__address { font-size: 18px; font-weight: 300; line-height: 26px; color: var(--ink-mid); }

  .contacts {
    position: absolute; right: 75px; top: 236px;
    border-collapse: collapse; color: var(--ink-mid);
    font-size: 17px;
  }
  .contacts th { font-weight: 400; text-align: right; padding-right: 14px; }
  .contacts td { font-weight: 300; text-align: right; }
  .contacts th, .contacts td { height: 24.5px; line-height: 24.5px; }

  .email {
    position: absolute; right: 75px; top: 337px;
    font-size: 17px; color: var(--ink-dark); line-height: 24px;
  }
  .icon { position: absolute; width: 23px; height: 23px; right: 39px; }
  .icon--phone { top: 238px; }
  .icon--mail { top: 340px; }
</style>
</head>
<body>
  <section class="card card--front">
    <div class="brand">
      <div class="brand__mark"></div>
      <div class="brand__name">TORVEL</div>
    </div>

    <div class="company">
      <div class="company__name">TORVEL Building and Plastering</div>
      <div class="company__address">PO BOX 57390 Marlowe Darwin NT 0815</div>
    </div>

    <table class="contacts">
      <tr><th>PH/Fax:</th><td>08 89317725</td></tr>
      <tr><th>Dale:</th><td>0417396248</td></tr>
      <tr><th>Rosa:</th><td>0409273516</td></tr>
      <tr><th>ABN:</th><td>58 297 130 846</td></tr>
    </table>
    <div class="email">torvel@quellnet.com</div>

    <svg class="icon icon--phone" viewBox="0 0 24 24" aria-hidden="true">
      <circle cx="12" cy="12" r="11" fill="var(--brand-blue)"/>
      <path d="M9 6.5c1 0 1.6 2.4 1.2 3-.3.5-1 .6-1 1.2 0 1 1.6 3 2.6 3 .6 0 .8-.8 1.3-1 .7-.2 2.9.7 2.9 1.6 0 .8-1.4 2.3-2.6 2.3C10 17.6 6.4 13.6 6.4 10 6.4 8 7.9 6.5 9 6.5z" fill="#fff"/>
    </svg>
    <svg class="icon icon--mail" viewBox="0 0 24 24" aria-hidden="true">
      <circle cx="12" cy="12" r="11" fill="var(--brand-blue)"/>
      <rect x="6" y="8" width="12" height="8.5" fill="none" stroke="#fff" stroke-width="1.3"/>
      <path d="M6 8l6 5 6-5" fill="none" stroke="#fff" stroke-width="1.3"/>
    </svg>
  </section>

  <section class="card card--back">
    <div class="brand">
      <div class="brand__mark"></div>
      <div class="brand__name">TORVEL</div>
    </div>
  </section>
</body>
</html>
```